Instant Broth for Ramen and Soup - Need labels for three flavors

We are a new company planning to launch a line of all natural powdered instant broth for ramen and soups. We need a logo design for our three launch flavors which will be Chicken, Prime Beef and Garden Vegetable. The powdered broth will be sold in 4oz containers with a white cap.
We would like the logo to be at the top of the label and or product description "Instant Broth for Ramen and Soups" underneath. The product description should stand out to the consumer, so it should likely be a larger font and one that compliments the logo. Below the Product description, we would like the name of the flavor and appropriate color scheme to match the flavor (see product picture for color). The design for each flavor should be the same, the only thing that should change is the color scheme to match flavor. Because we use all natural ingredients we would also like the label to state "Natural Ingredients" and "Gluten Free" on the front.
Additionally if you could please include placeholders for the nutritional label, ingredients list beneath, net size/weight on the side, bar code and a placeholder address for "Veltmore Foods LLC" that would be great as we are still finalizing these details. We would also like the label design to be catchy and interesting while complimenting the fun light-hearted logo.
Lastly, if your design is chosen you will be our main choice for additional design work (if you wish) including, top label design for the cap, finalizing the product info, formatting actual jar dimensions and other design work for the many other additional flavors we will be releasing.
Target Market(s)
Homemade ramen and soup connoisseurs, health conscious consumers, millennials and college students
Industry/Entity Type
It Company
Other font styles liked:
- SingleSleeve
Colors
Designer to choose colors to be used in the design.
Requirements
Must have
- 1) Logo
- 2) Product description "Instant Broth for Ramen and Soups"
- 3) Flavor title and color scheme
- 4) "Natural Ingredients" and "Gluten Free"
- 5) Place holder info for FDA required information (nutrition facts, net weight etc.)
Nice to have
- 1) Instructions (placeholder)
- 2) Additional info about the product (placeholder)

```html
<!DOCTYPE html>
<html lang="en">
<head>
<meta charset="utf-8">
<title>Brothwell Instant Broth – Flavor Labels</title>
<link rel="stylesheet" href="https://fonts.googleapis.com/css2?family=Montserrat:ital,wght@0,800;0,900;1,800&family=Roboto+Condensed:wght@400&display=swap">
<style>
  :root {
    --stage-top: #e2e0da;
    --stage-bottom: #ffffff;
    --label-base: #ffffff;
    --banner-ink: #0c0c0c;
    --banner-text: #ffffff;
    --brand-ink: #111111;
    --gluten-red: #e0141b;
    --badge-green: #3f7d1c;
    --badge-ring: #2b5a12;
    --spice-sage: #6f7f58;
    --spice-sand: #cbb98f;
    --spice-curry: #d8ad2c;
    --spice-pepper: #e6ddc4;
  }
  * { margin: 0; padding: 0; box-sizing: border-box; }
  html, body { width: 1200px; height: 593px; overflow: hidden; }
  body {
    background: linear-gradient(180deg, var(--stage-top), var(--stage-bottom));
    display: flex;
    align-items: center;
    justify-content: center;
    gap: 56px;
    padding-bottom: 40px;
  }
  .flavor-label {
    width: 304px;
    height: 222px;
    display: block;
    box-shadow: 0 6px 18px rgba(0,0,0,0.12);
  }
  .flavor-chicken { --tone-light: #eac51b; --tone-deep: #7b5b07; --art: #c9392f; }
  .flavor-beef    { --tone-light: #cd8a70; --tone-deep: #5a2410; --art: #d6336c; }
  .flavor-veg     { --tone-light: #93c53c; --tone-deep: #3f6e12; --art: #d9472b; }

  .label-base { fill: var(--label-base); }
  .tone-disc { fill: var(--tone-deep); opacity: 0.9; }
  .banner { fill: var(--banner-ink); }
  .banner-text {
    font-family: "Montserrat", sans-serif;
    font-weight: 800;
    font-size: 15px;
    fill: var(--banner-text);
    text-anchor: middle;
  }
  .brand-name {
    font-family: "Montserrat", sans-serif;
    font-weight: 900;
    font-size: 19px;
    fill: var(--brand-ink);
    text-anchor: middle;
  }
  .natural-badge { fill: var(--badge-green); stroke: var(--badge-ring); stroke-width: 2.5; }
  .badge-text {
    font-family: "Montserrat", sans-serif;
    font-weight: 800;
    fill: #ffffff;
    text-anchor: middle;
  }
  .badge-text.badge-big { font-size: 8px; }
  .badge-text.badge-small { font-size: 5.5px; }
  .gluten-free {
    font-family: "Montserrat", sans-serif;
    font-weight: 800;
    font-size: 12px;
    fill: var(--gluten-red);
  }
  .gluten-free .free-word { fill: #ffffff; font-style: italic; }
  .flavor-art { fill: var(--art); opacity: 0.9; }
  .flavor-name {
    font-family: "Roboto Condensed", sans-serif;
    font-size: 14px;
    fill: #ffffff;
    text-anchor: middle;
  }
</style>
</head>
<body>

<svg class="flavor-label flavor-chicken" viewBox="0 0 304 222" aria-label="Chicken flavor label">
  <defs>
    <linearGradient id="sweep-chicken" x1="0" x2="1">
      <stop offset="0" stop-color="var(--tone-light)"/>
      <stop offset="1" stop-color="#ffffff" stop-opacity="0.5"/>
    </linearGradient>
    <linearGradient id="spice-chicken" x1="0" x2="1">
      <stop offset="0" stop-color="var(--spice-sage)"/>
      <stop offset="0.35" stop-color="var(--spice-sand)"/>
      <stop offset="0.7" stop-color="var(--spice-curry)"/>
      <stop offset="1" stop-color="var(--spice-pepper)"/>
    </linearGradient>
  </defs>
  <rect class="label-base" width="304" height="222"/>
  <rect x="0" y="165" width="304" height="57" fill="url(#spice-chicken)" role="img" aria-label="Bowls of dried herbs and spices"/>
  <path d="M0,60 C60,20 190,25 304,80 L304,150 C230,170 120,160 0,185 Z" fill="url(#sweep-chicken)"/>
  <circle class="tone-disc" cx="150" cy="140" r="84"/>
  <text class="brand-name" x="150" y="36">BROTHWELL</text>
  <circle class="natural-badge" cx="264" cy="30" r="19"/>
  <text class="badge-text badge-big" x="264" y="29">100%</text>
  <text class="badge-text badge-small" x="264" y="37">NATURAL</text>
  <path class="banner" d="M30,72 C95,50 205,70 276,56 L272,108 C205,124 100,104 34,124 Z"/>
  <text class="banner-text" x="152" y="88">INSTANT BROTH</text>
  <text class="banner-text" x="152" y="106">FOR RAMEN AND SOUPS</text>
  <text class="gluten-free" x="12" y="152">Gluten<tspan class="free-word"> Free</tspan></text>
  <circle class="flavor-art" cx="160" cy="150" r="22" role="img" aria-label="Rooster head illustration"/>
  <text class="flavor-name" x="160" y="194">chicken</text>
</svg>

<svg class="flavor-label flavor-beef" viewBox="0 0 304 222" aria-label="Prime Beef flavor label">
  <defs>
    <linearGradient id="sweep-beef" x1="0" x2="1">
      <stop offset="0" stop-color="var(--tone-light)"/>
      <stop offset="1" stop-color="#ffffff" stop-opacity="0.5"/>
    </linearGradient>
    <linearGradient id="spice-beef" x1="0" x2="1">
      <stop offset="0" stop-color="var(--spice-sage)"/>
      <stop offset="0.35" stop-color="var(--spice-sand)"/>
      <stop offset="0.7" stop-color="var(--spice-curry)"/>
      <stop offset="1" stop-color="var(--spice-pepper)"/>
    </linearGradient>
  </defs>
  <rect class="label-base" width="304" height="222"/>
  <rect x="0" y="165" width="304" height="57" fill="url(#spice-beef)" role="img" aria-label="Bowls of dried herbs and spices"/>
  <path d="M0,60 C60,20 190,25 304,80 L304,150 C230,170 120,160 0,185 Z" fill="url(#sweep-beef)"/>
  <circle class="tone-disc" cx="150" cy="140" r="84"/>
  <text class="brand-name" x="150" y="36">BROTHWELL</text>
  <circle class="natural-badge" cx="264" cy="30" r="19"/>
  <text class="badge-text badge-big" x="264" y="29">100%</text>
  <text class="badge-text badge-small" x="264" y="37">NATURAL</text>
  <path class="banner" d="M30,72 C95,50 205,70 276,56 L272,108 C205,124 100,104 34,124 Z"/>
  <text class="banner-text" x="152" y="88">INSTANT BROTH</text>
  <text class="banner-text" x="152" y="106">FOR RAMEN AND SOUPS</text>
  <text class="gluten-free" x="12" y="152">Gluten<tspan class="free-word"> Free</tspan></text>
  <circle class="flavor-art" cx="154" cy="150" r="22" role="img" aria-label="Cow head illustration"/>
  <text class="flavor-name" x="154" y="194">Prime Beef</text>
</svg>

<svg class="flavor-label flavor-veg" viewBox="0 0 304 222" aria-label="Garden Vegetable flavor label">
  <defs>
    <linearGradient id="sweep-veg" x1="0" x2="1">
      <stop offset="0" stop-color="var(--tone-light)"/>
      <stop offset="1" stop-color="#ffffff" stop-opacity="0.5"/>
    </linearGradient>
    <linearGradient id="spice-veg" x1="0" x2="1">
      <stop offset="0" stop-color="var(--spice-sage)"/>
      <stop offset="0.35" stop-color="var(--spice-sand)"/>
      <stop offset="0.7" stop-color="var(--spice-curry)"/>
      <stop offset="1" stop-color="var(--spice-pepper)"/>
    </linearGradient>
  </defs>
  <rect class="label-base" width="304" height="222"/>
  <rect x="0" y="165" width="304" height="57" fill="url(#spice-veg)" role="img" aria-label="Bowls of dried herbs and spices"/>
  <path d="M0,60 C60,20 190,25 304,80 L304,150 C230,170 120,160 0,185 Z" fill="url(#sweep-veg)"/>
  <circle class="tone-disc" cx="150" cy="140" r="84"/>
  <text class="brand-name" x="150" y="36">BROTHWELL</text>
  <circle class="natural-badge" cx="264" cy="30" r="19"/>
  <text class="badge-text badge-big" x="264" y="29">100%</text>
  <text class="badge-text badge-small" x="264" y="37">NATURAL</text>
  <path class="banner" d="M30,72 C95,50 205,70 276,56 L272,108 C205,124 100,104 34,124 Z"/>
  <text class="banner-text" x="152" y="88">INSTANT BROTH</text>
  <text class="banner-text" x="152" y="106">FOR RAMEN AND SOUPS</text>
  <text class="gluten-free" x="12" y="152">Gluten<tspan class="free-word"> Free</tspan></text>
  <circle class="flavor-art" cx="166" cy="146" r="22" role="img" aria-label="Tomatoes, corn, pepper and zucchini illustration"/>
  <text class="flavor-name" x="166" y="186">Garden</text>
  <text class="flavor-name" x="166" y="201">Vegetable</text>
</svg>

</body>
</html>
```